Powerpoint template for Marlow Brook Consulting

I need a powerpoint template for my business that would also work for Google slides.
I intermittently deliver training to people and I want a nice powerpoint template, that could also work in google docs to help make production easier and more seamless for me. I also sometimes product reports and analyses that are best done in powerpoint or Google slides. I need a title page, Title and content page, section heading page and any other pages that someone normally has!

Target Market(s)

Leaders and managers in medium to large companies. I provide training and coaching services to senior staff who have got 'stuck' and want help to find their way forward.

Font styles to use
Sans Serif

Requirements
Must have
• Colours and fonts to fit with logo please.
• Must include the logo and company name.
Nice to have
• a picture for the front?

```html
<!DOCTYPE html>
<html lang="en">
<head>
<meta charset="utf-8">
<title>Marlow Brook Consulting – Slide Template</title>
<link href="https://fonts.googleapis.com/css2?family=Open+Sans:wght@400;600;700&family=Roboto+Condensed:wght@700&display=swap" rel="stylesheet">
<style>
:root{
  --purple:#55349a;
  --purple-dark:#3f2680;
  --purple-soft:#7a5cc0;
  --teal:#1db394;
  --teal-dark:#129176;
  --ink:#444;
  --muted:#888;
  --stage:#e4e4e6;
  --paper:#fff;
  --rule:#9fdcd0;
}
*{box-sizing:border-box;margin:0;padding:0}
html,body{width:1200px;height:905px;overflow:hidden;background:var(--stage);font-family:"Open Sans",Arial,sans-serif;color:var(--ink)}
.deck{position:relative;width:1200px;height:905px}
.slide{position:absolute;width:248px;height:141px;background:var(--paper);overflow:hidden;box-shadow:0 1px 3px rgba(0,0,0,.18)}
.c1{left:74px}.c2{left:343px}.c3{left:612px}.c4{left:881px}
.r1{top:58px}.r2{top:223px}.r3{top:385px}.r4{top:544px}.r5{top:707px}
.abs{position:absolute}
.slide-title{position:absolute;left:9px;top:7px;font-family:"Roboto Condensed",Arial,sans-serif;font-weight:700;font-size:7px;color:var(--purple);letter-spacing:.1px}
.slide-title::after{content:"";position:absolute;left:0;top:10px;width:13px;height:1px;background:var(--teal)}
.footer{position:absolute;left:20px;right:8px;top:132px;height:.6px;background:var(--rule)}
.mark{position:absolute;left:9px;top:129px;width:5px;height:5px;border-radius:50%;background:var(--teal)}
.pnum{position:absolute;right:6px;top:130px;font-size:2.5px;color:var(--muted)}
.tiny{font-size:2.6px;line-height:3.4px;color:var(--muted)}
.small{font-size:3.4px;line-height:4.2px}
.label{font-size:3.3px;font-weight:700;color:var(--purple)}
.photo{position:absolute}
.white{color:#fff}
.center{text-align:center}
.icon-dot{position:absolute;width:11px;height:11px;border-radius:50%}
</style>
</head>
<body>
<main class="deck">

<!-- 1 Cover -->
<section class="slide c1 r1" style="background:linear-gradient(180deg,#6d4fb0,#4a2c8d)">
  <div class="photo" role="img" aria-label="Silhouettes of business people shaking hands over a faint world map" style="inset:0;background:linear-gradient(90deg,rgba(40,20,90,.55),rgba(140,110,200,.25) 60%,rgba(90,60,160,.4))"></div>
  <div class="abs" style="left:99px;top:0;width:48px;height:66px;background:#fff;text-align:center">
    <div style="width:13px;height:13px;border-radius:50%;background:var(--teal);margin:14px auto 4px"></div>
    <div style="font-size:4.4px;font-weight:600;color:var(--purple);line-height:5px">Marlow Brook<br>Consulting</div>
  </div>
  <div class="abs white" style="left:0;right:0;top:97px;text-align:center;font-weight:700;font-size:11.5px">Marlow Brook Consulting</div>
</section>

<!-- 2 Title and content -->
<section class="slide c2 r1">
  <div class="slide-title">EDIT TITLE HERE</div>
  <div class="abs white" style="left:8px;top:31px;width:91px;height:90px;background:var(--purple);padding:12px 7px;font-size:3.9px;line-height:5px">Lorem ipsum dolor sit amet, consectetur adipiscing elit, sed do eiusmod tempor incididunt ut labore et dolore magna aliqua. Ut enim ad minim veniam, quis nostrud exercitation ullamco laboris nisi ut aliquip ex ea commodo consequat. Duis aute irure dolor in reprehenderit in voluptate velit esse cillum dolore eu fugiat nulla pariatur. Excepteur sint.</div>
  <div class="photo" role="img" aria-label="Overhead view of a team working with laptops and charts on a desk" style="left:99px;top:31px;width:149px;height:90px;background:linear-gradient(135deg,#8b8f96,#cfd3d8 45%,#6c7178)"></div>
  <div class="mark"></div><div class="footer"></div><div class="pnum">2</div>
</section>

<!-- 3 Team -->
<section class="slide c3 r1">
  <div class="slide-title">EDIT TITLE HERE</div>
  <div class="photo" role="img" aria-label="Portrait of Clara Hewitt" style="left:27px;top:37px;width:35px;height:35px;border-radius:50%;background:radial-gradient(#cfcfcf,#8d8d8d)"></div>
  <div class="photo" role="img" aria-label="Portrait of Tomas Reyes" style="left:79px;top:37px;width:35px;height:35px;border-radius:50%;background:radial-gradient(#d9c3ae,#8a705c)"></div>
  <div class="photo" role="img" aria-label="Portrait of Owen Patel" style="left:131px;top:37px;width:35px;height:35px;border-radius:50%;background:radial-gradient(#c9a98c,#6e5240)"></div>
  <div class="photo" role="img" aria-label="Portrait of Martin K Lowe" style="left:183px;top:37px;width:35px;height:35px;border-radius:50%;background:radial-gradient(#ddd,#9a9a9a)"></div>
  <div class="abs center" style="left:22px;top:76px;width:45px"><div class="label">Clara Hewitt</div><div class="tiny">Chief Business Officer</div></div>
  <div class="abs center" style="left:74px;top:76px;width:45px"><div class="label">Tomas Reyes</div><div class="tiny">Vice President</div></div>
  <div class="abs center" style="left:126px;top:76px;width:45px"><div class="label">Owen Patel</div><div class="tiny">Chief Medical Officer</div></div>
  <div class="abs center" style="left:175px;top:76px;width:51px"><div class="label">Martin K Lowe</div><div class="tiny">President and CEO</div></div>
  <div class="abs tiny center" style="left:18px;top:92px;width:212px">Lorem ipsum dolor sit amet, consectetur adipiscing elit. Nullam vitae lacus nec urna fermentum tempor sed quis magna. Integer posuere, sapien at luctus faucibus, nibh lectus pretium metus, non gravida risus arcu vel tortor. Praesent sodales augue vitae est tincidunt, ac placerat justo hendrerit sed.</div>
  <div class="mark"></div><div class="footer"></div><div class="pnum">3</div>
</section>

<!-- 4 Three images -->
<section class="slide c4 r1">
  <div class="slide-title">EDIT TITLE HERE</div>
  <div class="photo" role="img" aria-label="Laptop and monitors on a work desk" style="left:11px;top:24px;width:72px;height:57px;background:linear-gradient(135deg,#5e6670,#c6ccd2)"></div>
  <div class="photo" role="img" aria-label="Hand holding a tablet showing charts" style="left:88px;top:24px;width:72px;height:57px;background:linear-gradient(135deg,#dfe7ef,#8fb3d3)"></div>
  <div class="photo" role="img" aria-label="Colleagues meeting around a table" style="left:166px;top:24px;width:72px;height:57px;background:linear-gradient(135deg,#7a7f86,#bfc5cb)"></div>
  <div class="abs" style="left:11px;top:81px;width:227px;height:2px;background:var(--teal)"></div>
  <div class="abs center" style="left:11px;top:88px;width:72px"><div class="label">Lorem ipsum dolor</div><div class="tiny">Lorem ipsum dolor sit amet, consectetur adipiscing elit. Curabitur odio ligula, ultrices eu convallis et, felis ullamcorper interdum.</div></div>
  <div class="abs center" style="left:88px;top:88px;width:72px"><div class="label">Lorem ipsum dolor</div><div class="tiny">Lorem ipsum dolor sit amet, consectetur adipiscing elit. Curabitur odio ligula, ultrices eu convallis et, felis ullamcorper interdum.</div></div>
  <div class="abs center" style="left:166px;top:88px;width:72px"><div class="label">Lorem ipsum dolor</div><div class="tiny">Lorem ipsum dolor sit amet, consectetur adipiscing elit. Curabitur odio ligula, ultrices eu convallis et, felis ullamcorper interdum.</div></div>
  <div class="mark"></div><div class="footer"></div><div class="pnum">4</div>
</section>

<!-- 5 Icon grid -->
<section class="slide c1 r2">
  <div class="slide-title">EDIT TITLE HERE</div>
  <svg class="abs" style="left:0;top:0" width="248" height="141" viewBox="0 0 248 141" aria-hidden="true">
    <g fill="var(--teal)">
      <circle cx="41" cy="37" r="3.5"/><circle cx="82" cy="37" r="3.5"/><rect x="119" y="34" width="7" height="6"/><circle cx="164" cy="37" r="3.5"/><rect x="201" y="34.5" width="8" height="5"/>
      <circle cx="41" cy="82" r="3.5" fill="none" stroke="var(--teal)" stroke-width="1"/><circle cx="82" cy="82" r="3"/><rect x="119" y="79" width="7" height="6" rx="1"/><rect x="160" y="79" width="7" height="6" fill="none" stroke="var(--teal)" stroke-width="1"/><path d="M202 78h4v4h2l-4 4-4-4h2z"/>
    </g>
  </svg>
  <div class="abs" style="left:21px;top:44px;width:208px;display:grid;grid-template-columns:repeat(5,1fr);column-gap:6px;row-gap:24px">
    <div class="center"><div class="label" style="font-size:2.9px;color:var(--ink)">LOREM IPSUM</div><div class="tiny">Lorem ipsum dolor sit amet, consectetur adipiscing elit, sed do tempor</div></div>
    <div class="center"><div class="label" style="font-size:2.9px;color:var(--ink)">LOREM IPSUM</div><div class="tiny">Lorem ipsum dolor sit amet, consectetur adipiscing elit, sed do tempor</div></div>
    <div class="center"><div class="label" style="font-size:2.9px;color:var(--ink)">LOREM IPSUM</div><div class="tiny">Lorem ipsum dolor sit amet, consectetur adipiscing elit, sed do tempor</div></div>
    <div class="center"><div class="label" style="font-size:2.9px;color:var(--ink)">LOREM IPSUM</div><div class="tiny">Lorem ipsum dolor sit amet, consectetur adipiscing elit, sed do tempor</div></div>
    <div class="center"><div class="label" style="font-size:2.9px;color:var(--ink)">LOREM IPSUM</div><div class="tiny">Lorem ipsum dolor sit amet, consectetur adipiscing elit, sed do tempor</div></div>
    <div class="center"><div class="label" style="font-size:2.9px;color:var(--ink)">LOREM IPSUM</div><div class="tiny">Lorem ipsum dolor sit amet, consectetur adipiscing elit, sed do tempor</div></div>
    <div class="center"><div class="label" style="font-size:2.9px;color:var(--ink)">LOREM IPSUM</div><div class="tiny">Lorem ipsum dolor sit amet, consectetur adipiscing elit, sed do tempor</div></div>
    <div class="center"><div class="label" style="font-size:2.9px;color:var(--ink)">LOREM IPSUM</div><div class="tiny">Lorem ipsum dolor sit amet, consectetur adipiscing elit, sed do tempor</div></div>
    <div class="center"><div class="label" style="font-size:2.9px;color:var(--ink)">LOREM IPSUM</div><div class="tiny">Lorem ipsum dolor sit amet, consectetur adipiscing elit, sed do tempor</div></div>
    <div class="center"><div class="label" style="font-size:2.9px;color:var(--ink)">LOREM IPSUM</div><div class="tiny">Lorem ipsum dolor sit amet, consectetur adipiscing elit, sed do tempor</div></div>
  </div>
  <div class="mark"></div><div class="footer"></div><div class="pnum">5</div>
</section>

<!-- 6 Text and chart -->
<section class="slide c2 r2">
  <div class="slide-title">EDIT TITLE HERE</div>
  <div class="abs tiny" style="left:11px;top:25px;width:115px;color:#666">Lorem ipsum dolor sit amet, consectetur adipiscing elit, sed do eiusmod tempor incididunt ut labore et dolore magna aliqua. Ut enim ad minim veniam, quis nostrud exercitation ullamco laboris nisi ut aliquip ex ea commodo consequat. Duis aute irure dolor in reprehenderit in voluptate velit esse cillum dolore eu fugiat nulla pariatur. Excepteur sint occaecat cupidatat non proident, sunt in culpa qui officia deserunt mollit anim id est laborum. Sed ut perspiciatis unde omnis iste natus error sit voluptatem accusantium doloremque laudantium, totam rem aperiam, eaque ipsa quae ab illo inventore veritatis et quasi architecto beatae vitae dicta sunt explicabo. Nemo enim ipsam voluptatem quia voluptas sit aspernatur aut odit aut fugit, sed quia consequuntur magni dolores eos qui ratione voluptatem sequi nesciunt. Neque porro quisquam est, qui dolorem ipsum quia dolor sit amet.</div>
  <svg class="abs" style="left:128px;top:40px" width="115" height="80" viewBox="0 0 115 80" aria-label="Bar chart of yearly results">
    <line x1="14" y1="4" x2="14" y2="62" stroke="#ccc" stroke-width=".4"/>
    <line x1="14" y1="62" x2="108" y2="62" stroke="#ccc" stroke-width=".4"/>
    <g fill="var(--purple)">
      <rect x="18" y="52" width="9" height="10"/><rect x="31" y="41" width="9" height="21"/><rect x="44" y="26" width="9" height="36"/><rect x="57" y="17" width="9" height="45"/><rect x="70" y="24" width="9" height="38"/><rect x="83" y="37" width="9" height="25"/>
    </g>
    <polyline points="22,50 35,38 48,22 61,14 74,18 87,30 96,33" fill="none" stroke="#999" stroke-width=".4" stroke-dasharray="1 1"/>
    <rect x="54" y="6" width="15" height="5" fill="var(--teal)"/>
    <text x="61.5" y="9.8" font-size="2.8" fill="#fff" text-anchor="middle" font-family="Open Sans, sans-serif" font-weight="700">LOREM</text>
    <g font-size="2.2" fill="#999" font-family="Open Sans, sans-serif" text-anchor="middle">
      <text x="22.5" y="66">2011</text><text x="35.5" y="66">2012</text><text x="48.5" y="66">2013</text><text x="61.5" y="66">2014</text><text x="74.5" y="66">2015</text><text x="87.5" y="66">2016</text>
      <text x="61" y="71">Edit title here</text>
    </g>
  </svg>
  <div class="mark"></div><div class="footer"></div><div class="pnum">6</div>
</section>

<!-- 7 Section title -->
<section class="slide c3 r2" style="background:var(--teal)">
  <div class="photo" role="img" aria-label="Empty glass-walled conference room in teal tint" style="inset:0;background:linear-gradient(180deg,rgba(255,255,255,.25),rgba(29,179,148,.2) 55%,rgba(18,145,118,.6))"></div>
  <svg class="abs" style="left:27px;top:94px" width="22" height="18" viewBox="0 0 22 18" aria-hidden="true">
    <rect x="1" y="4" width="20" height="13" rx="1.5" fill="#fff"/><rect x="7.5" y="1" width="7" height="4" rx="1" fill="none" stroke="#fff" stroke-width="1.4"/><rect x="1" y="8" width="20" height="1" fill="var(--teal)"/>
  </svg>
  <div class="abs white" style="left:56px;top:92px;font-size:9.5px;font-weight:600">Section Title</div>
  <div class="abs tiny" style="left:56px;top:104px;width:90px;color:#e7fffa">Lorem ipsum dolor sit amet, consectetur adipiscing elit, sed do eiusmod tempor incididunt ut</div>
</section>

<!-- 8 Two columns -->
<section class="slide c4 r2">
  <div class="slide-title">EDIT TITLE HERE</div>
  <div class="abs white" style="left:14px;top:32px;width:111px;height:79px;background:var(--teal);padding:6px 8px 0 12px;font-size:3.2px;line-height:4px;font-weight:600">• Lorem ipsum dolor sit amet, consectetur adipiscing elit, sed do eiusmod tempor incididunt ut labore et dolore magna aliqua. Ut enim ad minim veniam, quis nostrud exercitation ullamco laboris nisi ut aliquip ex ea commodo consequat. Duis aute irure dolor in reprehenderit in voluptate velit esse cillum dolore eu fugiat nulla pariatur. Excepteur sint occaecat cupidatat non proident, sunt in culpa qui officia deserunt mollit anim id est laborum. Duis aute irure dolor in reprehenderit in voluptate velit esse cillum dolore eu fugiat nulla pariatur</div>
  <div class="abs white" style="left:127px;top:32px;width:110px;height:79px;background:var(--purple);padding:6px 8px 0 10px;font-size:3.2px;line-height:4px;font-weight:600">• Lorem ipsum dolor sit amet, consectetur adipiscing elit, sed do eiusmod tempor incididunt ut labore et dolore magna aliqua. Ut enim ad minim veniam, quis nostrud exercitation ullamco laboris nisi ut aliquip ex ea commodo consequat. Duis aute irure dolor in reprehenderit in voluptate velit esse cillum dolore eu fugiat nulla pariatur. Excepteur sint occaecat cupidatat non proident, sunt in culpa qui officia deserunt mollit anim id est laborum.<br>• Duis aute irure dolor in reprehenderit in voluptate velit esse cillum dolore eu fugiat nulla pariatur</div>
  <div class="abs" style="left:14px;top:111px;width:223px;height:2px;background:var(--purple-dark)"></div>
  <div class="mark"></div><div class="footer"></div><div class="pnum">8</div>
</section>

<!-- 9 Icon list -->
<section class="slide c1 r3">
  <div class="slide-title">EDIT TITLE HERE</div>
  <div class="abs" style="left:124px;top:30px;width:.5px;height:95px;background:#ccc"></div>
  <div class="icon-dot" style="left:113px;top:34px;background:var(--purple)"></div>
  <div class="icon-dot" style="left:113px;top:59px;background:var(--purple)"></div>
  <div class="icon-dot" style="left:113px;top:84px;background:var(--purple)"></div>
  <div class="icon-dot" style="left:113px;top:109px;background:var(--purple)"></div>
  <div class="icon-dot" style="left:132px;top:34px;background:var(--teal)"></div>
  <div class="icon-dot" style="left:132px;top:59px;background:var(--teal)"></div>
  <div class="icon-dot" style="left:132px;top:84px;background:var(--teal)"></div>
  <div class="icon-dot" style="left:132px;top:109px;background:var(--teal)"></div>
  <div class="abs" style="left:30px;top:34px;width:80px;text-align:right">
    <div class="label">Lorem ipsum dolor</div><div class="tiny">Lorem ipsum dolor sit amet, consectetur<br>adipiscing elit, sed do eiusmod tempor</div>
    <div class="label" style="margin-top:10px">Lorem ipsum dolor</div><div class="tiny">Lorem ipsum dolor sit amet, consectetur<br>adipiscing elit, sed do eiusmod tempor</div>
    <div class="label" style="margin-top:10px">Lorem ipsum dolor</div><div class="tiny">Lorem ipsum dolor sit amet, consectetur<br>adipiscing elit, sed do eiusmod tempor</div>
    <div class="label" style="margin-top:10px">Lorem ipsum dolor</div><div class="tiny">Lorem ipsum dolor sit amet, consectetur<br>adipiscing elit, sed do eiusmod tempor</div>
  </div>
  <div class="abs" style="left:146px;top:34px;width:85px">
    <div class="label">Lorem ipsum dolor</div><div class="tiny">Lorem ipsum dolor sit amet, consectetur<br>adipiscing elit, sed do eiusmod tempor</div>
    <div class="label" style="margin-top:10px">Lorem ipsum dolor</div><div class="tiny">Lorem ipsum dolor sit amet, consectetur<br>adipiscing elit, sed do eiusmod tempor</div>
    <div class="label" style="margin-top:10px">Lorem ipsum dolor</div><div class="tiny">Lorem ipsum dolor sit amet, consectetur<br>adipiscing elit, sed do eiusmod tempor</div>
    <div class="label" style="margin-top:10px">Lorem ipsum dolor</div><div class="tiny">Lorem ipsum dolor sit amet, consectetur<br>adipiscing elit, sed do eiusmod tempor</div>
  </div>
  <div class="mark"></div><div class="footer"></div><div class="pnum">9</div>
</section>

<!-- 10 Card over image -->
<section class="slide c2 r3">
  <div class="slide-title">EDIT TITLE HERE</div>
  <div class="photo" role="img" aria-label="Modern office interior with chairs" style="left:8px;top:22px;width:240px;height:102px;background:linear-gradient(135deg,#dfe6ec,#a9b8c4)"></div>
  <div class="abs" style="left:8px;top:22px;width:141px;height:102px;background:rgba(85,52,154,.92)"></div>
  <div class="abs white" style="left:19px;top:42px;width:44px;font-size:3.6px;line-height:4.4px;font-weight:600;text-align:center">Lorem ipsum dolor sit amet consectetur adipiscing elit. Cras bibendum mattis leo, ac efficitur ipsum lobortis non. Praesent vitae pulvinar lorem ipsum dolor sit amet consectetur adipiscing elit.</div>
  <div class="abs" style="left:70px;top:43px;width:165px;height:60px;background:#fff"></div>
  <svg class="abs" style="left:70px;top:43px" width="165" height="60" viewBox="0 0 165 60" aria-hidden="true">
    <g fill="var(--teal)">
      <rect x="29" y="12" width="3" height="12"/><rect x="33" y="9" width="5" height="15"/><rect x="39" y="15" width="3" height="9"/>
      <rect x="76" y="12" width="12" height="11" rx="1.5"/><rect x="79" y="9" width="6" height="3" fill="none" stroke="var(--teal)" stroke-width="1"/>
      <rect x="120" y="14" width="14" height="7" rx="2"/><rect x="122" y="10" width="10" height="5" rx="1"/><circle cx="123" cy="22" r="1.6"/><circle cx="131" cy="22" r="1.6"/>
    </g>
    <rect x="81" y="15" width="2" height="6" fill="#fff"/><rect x="79" y="17" width="6" height="2" fill="#fff"/>
    <g font-family="Open Sans, sans-serif" font-size="3.6" font-weight="700" fill="#555" text-anchor="middle">
      <text x="35.5" y="33">LOREM</text><text x="82" y="33">LOREM</text><text x="127" y="33">LOREM</text>
    </g>
  </svg>
  <div class="mark"></div><div class="footer"></div><div class="pnum">10</div>
</section>

<!-- 11 Puzzle -->
<section class="slide c3 r3">
  <div class="slide-title">EDIT TITLE HERE</div>
  <div class="photo" role="img" aria-label="Four interlocking puzzle pieces in teal and purple" style="left:76px;top:32px;width:82px;height:82px;background:radial-gradient(circle at 35% 40%,var(--teal),var(--purple) 75%);border-radius:8px;opacity:.9"></div>
  <div class="abs" style="left:149px;top:29px;width:70px"><div class="label">Lorem ipsum dolor sit</div><div class="tiny">Lorem ipsum dolor sit amet,<br>consectetur adipiscing elit, sed</div></div>
  <div class="abs" style="left:16px;top:65px;width:58px;text-align:right"><div class="label">Lorem ipsum dolor sit</div><div class="tiny">Lorem ipsum dolor sit amet,<br>consectetur adipiscing elit, sed</div></div>
  <div class="abs" style="left:168px;top:74px;width:70px"><div class="label">Lorem ipsum dolor sit</div><div class="tiny">Lorem ipsum dolor sit amet,<br>consectetur adipiscing elit, sed</div></div>
  <div class="abs" style="left:37px;top:101px;width:60px;text-align:right"><div class="label">Lorem ipsum dolor sit</div><div class="tiny">Lorem ipsum dolor sit amet,<br>consectetur adipiscing elit, sed</div></div>
  <div class="mark"></div><div class="footer"></div><div class="pnum">11</div>
</section>

<!-- 12 Text with image and boxes -->
<section class="slide c4 r3">
  <div class="slide-title">EDIT TITLE HERE</div>
  <div class="abs tiny" style="left:11px;top:33px;width:63px;color:#666">Lorem ipsum dolor sit amet, consectetur adipiscing elit. Donec lorem ante, laoreet et ac, sollicitudin maximus felis. Curabitur dictum, turpis ac ultricies rutrum, lectus sapien cursus est, vitae suscipit odio justo eget sem. Vestibulum enim ante, ultricies quis placerat sed, aliquam eu ipsum. Sed a felis et diam ullamcorper convallis eu ut diam. Nam rhoncus risus a felis maximus aliquet. Integer quis tincidunt libero, non tincidunt ligula. Lorem ipsum dolor sit amet, consectetur adipiscing elit. Donec lorem ante, laoreet et ac, sollicitudin maximus felis.</div>
  <div class="photo" role="img" aria-label="Abstract blue molecular network background" style="left:121px;top:22px;width:127px;height:102px;background:radial-gradient(circle at 70% 35%,#7fa7e8,#3b4fb0 55%,#2a2e7a)"></div>
  <div class="abs white" style="left:78px;top:33px;width:74px;height:80px;background:var(--teal);padding:3px 5px;font-size:2.6px;line-height:3.3px;text-align:center"><div style="font-weight:700;font-size:3.3px;margin-bottom:2px">Lorem ipsum</div>Lorem ipsum dolor sit amet, consectetur adipiscing elit. Donec lorem ante, laoreet et ac, sollicitudin maximus felis. Curabitur dictum, turpis ac ultricies rutrum, lectus sapien cursus est, vitae suscipit odio justo eget sem. Vestibulum enim ante, ultricies quis placerat sed, aliquam eu ipsum. Sed a felis et diam ullamcorper convallis eu ut diam.</div>
  <div class="abs white" style="left:155px;top:33px;width:74px;height:80px;background:var(--teal);padding:3px 5px;font-size:2.6px;line-height:3.3px;text-align:center"><div style="font-weight:700;font-size:3.3px;margin-bottom:2px">Lorem ipsum</div>Lorem ipsum dolor sit amet, consectetur adipiscing elit. Donec lorem ante, laoreet et ac, sollicitudin maximus felis. Curabitur dictum, turpis ac ultricies rutrum, lectus sapien cursus est, vitae suscipit odio justo eget sem. Vestibulum enim ante, ultricies quis placerat sed, aliquam eu ipsum. Sed a felis et diam ullamcorper convallis eu ut diam.</div>
  <div class="mark"></div><div class="footer"></div><div class="pnum">12</div>
</section>

<!-- 13 Two process columns -->
<section class="slide c1 r4">
  <div class="slide-title">EDIT TITLE HERE</div>
  <svg class="abs" style="left:0;top:0" width="248" height="141" viewBox="0 0 248 141" aria-label="Two three-step process lists">
    <rect x="30" y="29" width="83" height="7" fill="var(--teal)"/>
    <rect x="133" y="29" width="84" height="7" fill="var(--purple)"/>
    <line x1="35" y1="36" x2="35" y2="113" stroke="var(--teal)" stroke-width=".6"/>
    <line x1="138" y1="36" x2="138" y2="113" stroke="var(--purple)" stroke-width=".6"/>
    <g fill="var(--teal)">
      <circle cx="35" cy="57" r="3.5"/><circle cx="35" cy="85" r="3.5"/><circle cx="35" cy="113" r="3.5"/>
      <rect x="47" y="48" width="66" height="19" rx="2"/><rect x="47" y="76" width="66" height="19" rx="2"/><rect x="47" y="104" width="66" height="19" rx="2"/>
      <path d="M39 57h8M39 85h8M39 113h8" stroke="var(--teal)" stroke-width=".6"/>
      <path d="M47 55l-3 2 3 2zM47 83l-3 2 3 2zM47 111l-3 2 3 2z"/>
    </g>
    <g fill="var(--purple)">
      <circle cx="138" cy="57" r="3.5"/><circle cx="138" cy="85" r="3.5"/><circle cx="138" cy="113" r="3.5"/>
      <rect x="150" y="48" width="67" height="19" rx="2"/><rect x="150" y="76" width="67" height="19" rx="2"/><rect x="150" y="104" width="67" height="19" rx="2"/>
      <path d="M142 57h8M142 85h8M142 113h8" stroke="var(--purple)" stroke-width=".6"/>
      <path d="M150 55l-3 2 3 2zM150 83l-3 2 3 2zM150 111l-3 2 3 2z"/>
    </g>
    <g font-family="Open Sans, sans-serif" font-size="2.8" fill="#fff" text-anchor="middle" font-weight="700">
      <text x="71.5" y="33.8">LOREM IPSUM</text><text x="175" y="33.8">LOREM IPSUM</text>
    </g>
    <g font-family="Open Sans, sans-serif" font-size="3.4" fill="#fff" text-anchor="middle">
      <text x="80" y="56">Lorem ipsum dolor sit amet,</text><text x="80" y="60">consectetur adipiscing elit, sed do</text><text x="80" y="64">dolore magna aliqua.</text>
      <text x="80" y="84">Lorem ipsum dolor sit amet,</text><text x="80" y="88">consectetur adipiscing elit, sed do</text><text x="80" y="92">dolore magna aliqua.</text>
      <text x="80" y="112">Lorem ipsum dolor sit amet,</text><text x="80" y="116">consectetur adipiscing elit, sed do</text><text x="80" y="120">dolore magna aliqua.</text>
      <text x="183.5" y="56">Lorem ipsum dolor sit amet,</text><text x="183.5" y="60">consectetur adipiscing elit, sed do</text><text x="183.5" y="64">dolore magna aliqua.</text>
      <text x="183.5" y="84">Lorem ipsum dolor sit amet,</text><text x="183.5" y="88">consectetur adipiscing elit, sed do</text><text x="183.5" y="92">dolore magna aliqua.</text>
      <text x="183.5" y="112">Lorem ipsum dolor sit amet,</text><text x="183.5" y="116">consectetur adipiscing elit, sed do</text><text x="183.5" y="120">dolore magna aliqua.</text>
    </g>
  </svg>
  <div class="mark"></div><div class="footer"></div><div class="pnum">13</div>
</section>

<!-- 14 Timeline -->
<section class="slide c2 r4">
  <div class="slide-title">EDIT TITLE HERE</div>
  <svg class="abs" style="left:0;top:0" width="248" height="141" viewBox="0 0 248 141" aria-label="Timeline from 2011 to 2017">
    <line x1="34" y1="108" x2="218" y2="108" stroke="var(--purple)" stroke-width=".8"/>
    <g stroke-width=".8" fill="#fff">
      <circle cx="34" cy="73" r="14" stroke="var(--purple)"/><circle cx="65" cy="52" r="14" stroke="var(--teal)"/><circle cx="96" cy="67" r="14" stroke="var(--purple)"/><circle cx="127" cy="52" r="14" stroke="var(--teal)"/><circle cx="158" cy="67" r="14" stroke="var(--purple)"/><circle cx="189" cy="52" r="14" stroke="var(--teal)"/><circle cx="220" cy="67" r="14" stroke="var(--purple)"/>
    </g>
    <g stroke-width=".8">
      <line x1="34" y1="92" x2="34" y2="108" stroke="var(--purple)"/><line x1="65" y1="71" x2="65" y2="108" stroke="var(--teal)"/><line x1="96" y1="86" x2="96" y2="108" stroke="var(--purple)"/><line x1="127" y1="71" x2="127" y2="108" stroke="var(--teal)"/><line x1="158" y1="86" x2="158" y2="108" stroke="var(--purple)"/><line x1="189" y1="71" x2="189" y2="108" stroke="var(--teal)"/><line x1="220" y1="86" x2="220" y2="108" stroke="var(--purple)"/>
    </g>
    <g>
      <circle cx="34" cy="88" r="4" fill="var(--purple)"/><circle cx="65" cy="67" r="4" fill="var(--teal)"/><circle cx="96" cy="82" r="4" fill="var(--purple)"/><circle cx="127" cy="67" r="4" fill="var(--teal)"/><circle cx="158" cy="82" r="4" fill="var(--purple)"/><circle cx="189" cy="67" r="4" fill="var(--teal)"/><circle cx="220" cy="82" r="4" fill="var(--purple)"/>
      <circle cx="34" cy="108" r="1.3" fill="var(--purple)"/><circle cx="65" cy="108" r="1.3" fill="var(--teal)"/><circle cx="96" cy="108" r="1.3" fill="var(--purple)"/><circle cx="127" cy="108" r="1.3" fill="var(--teal)"/><circle cx="158" cy="108" r="1.3" fill="var(--purple)"/><circle cx="189" cy="108" r="1.3" fill="var(--teal)"/><circle cx="220" cy="108" r="1.3" fill="var(--purple)"/>
    </g>
    <g font-family="Open Sans, sans-serif" font-size="2.6" fill="#fff" text-anchor="middle" font-weight="700">
      <text x="34" y="89">2011</text><text x="65" y="68">2012</text><text x="96" y="83">2013</text><text x="127" y="68">2014</text><text x="158" y="83">2015</text><text x="189" y="68">2016</text><text x="220" y="83">2017</text>
    </g>
    <g font-family="Open Sans, sans-serif" font-size="2.6" fill="#333" text-anchor="middle" font-weight="700">
      <text x="34" y="66">Edit Title</text><text x="65" y="45">Edit Title</text><text x="96" y="60">Edit Title</text><text x="127" y="45">Edit Title</text><text x="158" y="60">Edit Title</text><text x="189" y="45">Edit Title</text><text x="220" y="60">Edit Title</text>
    </g>
    <g font-family="Open Sans, sans-serif" font-size="2" fill="#999" text-anchor="middle">
      <text x="34" y="70">Lorem ipsum dolor</text><text x="34" y="73">sit amet adipiscing</text><text x="34" y="76">elit sed do tempor</text>
      <text x="65" y="49">Lorem ipsum dolor</text><text x="65" y="52">sit amet adipiscing</text><text x="65" y="55">elit sed do tempor</text>
      <text x="96" y="64">Lorem ipsum dolor</text><text x="96" y="67">sit amet adipiscing</text><text x="96" y="70">elit sed do tempor</text>
      <text x="127" y="49">Lorem ipsum dolor</text><text x="127" y="52">sit amet adipiscing</text><text x="127" y="55">elit sed do tempor</text>
      <text x="158" y="64">Lorem ipsum dolor</text><text x="158" y="67">sit amet adipiscing</text><text x="158" y="70">elit sed do tempor</text>
      <text x="189" y="49">Lorem ipsum dolor</text><text x="189" y="52">sit amet adipiscing</text><text x="189" y="55">elit sed do tempor</text>
      <text x="220" y="64">Lorem ipsum dolor</text><text x="220" y="67">sit amet adipiscing</text><text x="220" y="70">elit sed do tempor</text>
    </g>
  </svg>
  <div class="mark"></div><div class="footer"></div><div class="pnum">14</div>
</section>

<!-- 15 Six columns -->
<section class="slide c3 r4">
  <div class="slide-title">EDIT TITLE HERE</div>
  <div class="abs" style="left:14px;top:35px;width:222px;display:grid;grid-template-columns:repeat(6,1fr);gap:4px">
    <div><div class="photo" role="img" aria-label="Business people in discussion" style="position:relative;height:38px;background:linear-gradient(135deg,#5d6169,#b9bec4)"></div><div class="white center" style="background:var(--purple-dark);font-size:2.6px;font-weight:700;padding:1px 0">TITLE HERE</div><div class="white" style="background:var(--purple);height:38px;font-size:2.1px;line-height:3.6px;padding:2px 3px">• Lorem ipsum dolor sit<br>• Lorem ipsum dolor sit<br>• Lorem ipsum dolor sit<br>• Lorem ipsum dolor sit<br>• Lorem ipsum dolor sit<br>• Lorem ipsum dolor sit<br>• Lorem ipsum dolor sit<br>• Lorem ipsum dolor sit</div></div>
    <div><div class="photo" role="img" aria-label="Clock on a desk" style="position:relative;height:38px;background:linear-gradient(135deg,#6a4a33,#d8b78e)"></div><div class="white center" style="background:var(--teal-dark);font-size:2.6px;font-weight:700;padding:1px 0">TITLE HERE</div><div class="white" style="background:var(--teal);height:38px;font-size:2.1px;line-height:3.6px;padding:2px 3px">• Lorem ipsum dolor sit<br>• Lorem ipsum dolor sit<br>• Lorem ipsum dolor sit<br>• Lorem ipsum dolor sit<br>• Lorem ipsum dolor sit<br>• Lorem ipsum dolor sit<br>• Lorem ipsum dolor sit<br>• Lorem ipsum dolor sit</div></div>
    <div><div class="photo" role="img" aria-label="Office workers at computers" style="position:relative;height:38px;background:linear-gradient(135deg,#8a96a6,#dde3ea)"></div><div class="white center" style="background:var(--purple-dark);font-size:2.6px;font-weight:700;padding:1px 0">TITLE HERE</div><div class="white" style="background:var(--purple);height:38px;font-size:2.1px;line-height:3.6px;padding:2px 3px">• Lorem ipsum dolor sit<br>• Lorem ipsum dolor sit<br>• Lorem ipsum dolor sit<br>• Lorem ipsum dolor sit<br>• Lorem ipsum dolor sit<br>• Lorem ipsum dolor sit<br>• Lorem ipsum dolor sit<br>• Lorem ipsum dolor sit</div></div>
    <div><div class="photo" role="img" aria-label="Professional in an office" style="position:relative;height:38px;background:linear-gradient(135deg,#c9ccd0,#7c8189)"></div><div class="white center" style="background:var(--teal-dark);font-size:2.6px;font-weight:700;padding:1px 0">TITLE HERE</div><div class="white" style="background:var(--teal);height:38px;font-size:2.1px;line-height:3.6px;padding:2px 3px">• Lorem ipsum dolor sit<br>• Lorem ipsum dolor sit<br>• Lorem ipsum dolor sit<br>• Lorem ipsum dolor sit<br>• Lorem ipsum dolor sit<br>• Lorem ipsum dolor sit<br>• Lorem ipsum dolor sit<br>• Lorem ipsum dolor sit</div></div>
    <div><div class="photo" role="img" aria-label="Computer screen with charts" style="position:relative;height:38px;background:linear-gradient(135deg,#e4ecf5,#7f98b8)"></div><div class="white center" style="background:var(--purple-dark);font-size:2.6px;font-weight:700;padding:1px 0">TITLE HERE</div><div class="white" style="background:var(--purple);height:38px;font-size:2.1px;line-height:3.6px;padding:2px 3px">• Lorem ipsum dolor sit<br>• Lorem ipsum dolor sit<br>• Lorem ipsum dolor sit<br>• Lorem ipsum dolor sit<br>• Lorem ipsum dolor sit<br>• Lorem ipsum dolor sit<br>• Lorem ipsum dolor sit<br>• Lorem ipsum dolor sit</div></div>
    <div><div class="photo" role="img" aria-label="Person working at a laptop" style="position:relative;height:38px;background:linear-gradient(135deg,#50555c,#a9aeb4)"></div><div class="white center" style="background:var(--teal-dark);font-size:2.6px;font-weight:700;padding:1px 0">TITLE HERE</div><div class="white" style="background:var(--teal);height:38px;font-size:2.1px;line-height:3.6px;padding:2px 3px">• Lorem ipsum dolor sit<br>• Lorem ipsum dolor sit<br>• Lorem ipsum dolor sit<br>• Lorem ipsum dolor sit<br>• Lorem ipsum dolor sit<br>• Lorem ipsum dolor sit<br>• Lorem ipsum dolor sit<br>• Lorem ipsum dolor sit</div></div>
  </div>
  <div class="mark"></div><div class="footer"></div><div class="pnum">15</div>
</section>

<!-- 16 A B C D -->
<section class="slide c4 r4">
  <div class="slide-title">EDIT TITLE HERE</div>
  <div class="abs" style="left:15px;top:22px;font-size:3.2px;color:#555">Lorem ipsum dolor sit amet, consectetur adipiscing elit. Aenean sed tempor lorem. Suspendisse</div>
  <div class="photo" role="img" aria-label="Group of smiling colleagues in front of a brick wall" style="left:15px;top:32px;width:220px;height:50px;background:linear-gradient(90deg,#6d7d4c,#a58a6c 40%,#8a5a48 70%,#6e7a55)"></div>
  <div class="abs" style="left:15px;top:88px;width:220px;display:grid;grid-template-columns:repeat(4,1fr);gap:7px">
    <div><div class="white center" style="background:var(--teal);font-size:4px;font-weight:700;padding:1.5px 0">A</div><div class="tiny center" style="margin-top:3px">Lorem ipsum dolor sit amet, consectetur adipiscing elit. Aenean sed tempor lorem. Suspendisse varius enim id euismod, quis condimentum risus</div></div>
    <div><div class="white center" style="background:var(--purple);font-size:4px;font-weight:700;padding:1.5px 0">B</div><div class="tiny center" style="margin-top:3px">Lorem ipsum dolor sit amet, consectetur adipiscing elit. Aenean sed tempor lorem. Suspendisse varius enim id euismod, quis condimentum risus</div></div>
    <div><div class="white center" style="background:var(--teal);font-size:4px;font-weight:700;padding:1.5px 0">C</div><div class="tiny center" style="margin-top:3px">Lorem ipsum dolor sit amet, consectetur adipiscing elit. Aenean sed tempor lorem. Suspendisse varius enim id euismod, quis condimentum risus</div></div>
    <div><div class="white center" style="background:var(--purple);font-size:4px;font-weight:700;padding:1.5px 0">D</div><div class="tiny center" style="margin-top:3px">Lorem ipsum dolor sit amet, consectetur adipiscing elit. Aenean sed tempor lorem. Suspendisse varius enim id euismod, quis condimentum risus</div></div>
  </div>
  <div class="mark"></div><div class="footer"></div><div class="pnum">16</div>
</section>

<!-- 17 Quote -->
<section class="slide c2 r5" style="background:#d9d9db">
  <div class="abs" style="left:0;top:0;width:248px;height:70px;background:linear-gradient(90deg,var(--purple),var(--purple-soft))"></div>
  <div class="abs white" style="left:11px;top:3px;font-size:14px;font-weight:700;line-height:14px">&ldquo;</div>
  <div class="abs white" style="right:9px;top:49px;font-size:14px;font-weight:700;line-height:14px">&rdquo;</div>
  <div class="abs white center" style="left:22px;top:20px;width:204px;font-size:5.3px;line-height:6.8px;font-weight:600">"Lorem ipsum dolor sit amet, consectetur adipiscing elit. Phasellus sodales, ligula ultrices tempus ristique, tellus justo aliquam dui, nec Lorem ipsum dolor sit amet, consectetur adipiscing elit. elit. Lorem ipsum dolor sit amet, consectetur sit amet, consectetur adipiscing"</div>
  <div class="photo" role="img" aria-label="Portrait of Harriet Vale" style="left:106px;top:56px;width:37px;height:37px;border-radius:50%;border:1.5px solid #fff;background:radial-gradient(#b99a82,#5b4638)"></div>
  <div class="abs center" style="left:0;right:0;top:102px;font-size:5px;font-weight:600;color:#444">Harriet Vale</div>
  <div class="abs center tiny" style="left:0;right:0;top:109px;font-style:normal">Chief Operating Officer</div>
</section>

<!-- 18 Thank you -->
<section class="slide c3 r5">
  <div class="photo" role="img" aria-label="Cheerful group of people holding speech bubbles" style="inset:0;background:linear-gradient(90deg,#c9a98f,#8f6e5a 35%,#b8876a 60%,#6f5a4e)"></div>
  <div class="abs" style="left:27px;top:0;width:96px;height:141px;background:rgba(85,52,154,.88)"></div>
  <div class="abs white center" style="left:27px;top:66px;width:96px;font-size:9.5px;font-weight:600">THANK YOU</div>
</section>

</main>
</body>
</html>
```